BELVORA needs a label for a Surface Cleaner with Alcohol

INTRODUCTION:
We are BELVORA, an experienced Spanish family-owned business specialized in manufacturing and distributing low-cost high-quality cleaning products in Spain, France and Portugal.

We are launching a new SURFACE CLEANER WITH ALCOHOL and we need an eye-catching label! We want to put your creativity to work! :D

CONCEPT:
Surface cleaner containing alcohol (not a disinfectant or hand sanitizer)

2 sizes

1) 750 ml PET cilinder white bottle with spray (bottle measures: 70mm diameter 230 mm height w/o spray)
Labels size (120mm base x 160mm height), 1 front label + 1 back label

2) 60 ml PET cilinder white bottle with spray (bottle 90mm height w/o spray x 35mm diameter) 1 label
Label size 110mm base x 60mm height

The design of the larger bottle must be adapted to the smaller bottle so as to make a collection

Label is in Spanish language (we are providing texts below)

GOAL:
To create a clean minimalist label with a “pharmaceutical” look and feel. Ideally by using colors and shapes to evoke a pharma green cross without explicitly using it. The pharma look and feel has to be visible from some distance. It must inspire safety and protection.

If you do mockups please use a 3D image of a bottle with sprayer (not the photo attached because it will look bad)

We love to see your ideas and be surprised with your proposals!

Thank you!

Target Market(s)

General public (non-professional) target, drugstore/supermaket, Spanish market mainly at the moment

Industry/Entity Type

Cleaning Product

Requirements
Must have
• Label front must have:
• - words: "LIMPIADOR HIGIENIZANTE" and "con ALCOHOL"
• - colors: white, pharma-looking light green, and a touch of blue
• - logo: BELVORA (brand), with the same pharma-looking green color
• - for the small bottle: a plane icon to point out that is suitable for travelling
• Label back side must contain this:
• - marketing text:
• “Limpiador higienizante para todo tipo de superfícies lavables. Su gran poder limpiador e higienizante elimina eficazmente la suciedad de zonas de contacto tales como asientos, inodoros, duchas, vidrios, pomos, manetas, asideros, barandillas, mesas, encimeras, suelos, mostradores, vitrinas, etc. No contiene lejía.”
• - icons:
• A column of 4-5 minimalist icons to clearly point out the applications (door knobs, seats, sink, handrail, toilet, floor, shower, glass,…) see icon examples attached for styling inspiration
• - legal text:
• “Líquido y vapores muy inflamables. Provoca irritación ocular grave. Puede provocar somnolencia o vértigo. Mantener alejado del calor, de superficies calientes, de chispas, de llamas abiertas y de cualquier otra fuente de ignición. No fumar. Mantener el recipiente herméticamente cerrado. Evitar respirar el polvo/el humo/el gas/la niebla/los vapores/el aerosol. Llevar guantes/prendas/gafas/máscara de protección. En caso de incendio emplear niebla de agua, espuma, productos químicos secos o dióxido de carbono ( CO2 ) para apagarlo. Almacenar en un lugar bien ventilado. Mantener el recipiente cerrado herméticamente. Mantener en lugar fresco.”
• - company identification:
• TOLMEN CASTRA SL
• B47392618
• C/ Valdemur 317 2-4
• 08051 Barcelona
• - pictograms: see the pictograms file
Nice to have
• Would be great to include:
• - seal: round seal with one or two words inside to give the feeling of “certified” or “approved”
• - a percetage number, like "100 % efectivo”
• - a small red “plus” sign referring for example to “+ higiene”
Should not have
• A plain green or red cross alone

```html
<!DOCTYPE html>
<html lang="es">
<head>
<meta charset="utf-8">
<title>BELVORA · Limpiador Higienizante con Alcohol · etiquetas</title>
<link rel="stylesheet" href="https://fonts.googleapis.com/css2?family=Oswald:wght@500;600&family=Open+Sans:wght@400;600;700&display=swap">
<style>
  :root{
    --page:#ffffff;
    --label:#f6f6f6;
    --teal:#12a08e;
    --teal-light:#45c1ad;
    --teal-dark:#0c8a7b;
    --blue:#1c6fb8;
    --blue-light:#2f86c8;
    --red:#e0282f;
    --seal-dark:#1e5b61;
    --ink:#2a2a2a;
    --ink-soft:#444;
    --frame:#555;
  }
  *{box-sizing:border-box;margin:0;padding:0}
  html,body{width:1200px;height:1200px;overflow:hidden;background:var(--page)}
  .canvas{position:relative;width:1200px;height:1200px}
  .label{position:absolute;top:170px;width:510px;height:860px;background:var(--label)}
  .label--front{left:70px}
  .label--back{left:620px}
  .band{position:absolute;left:0;width:100%;height:18px;background:linear-gradient(90deg,var(--teal-light),var(--teal-dark))}
  .band--top{top:0}
  .band--bottom{bottom:0}

  /* front */
  .title{position:absolute;top:64px;left:0;width:100%;text-align:center;font-family:'Oswald',sans-serif;font-weight:500;color:var(--teal);line-height:74px;text-transform:uppercase;font-size:68px;letter-spacing:0.5px}
  .claim{position:absolute;top:226px;left:0;width:100%;text-align:center;font-family:'Oswald',sans-serif;font-weight:500;color:var(--blue);line-height:1}
  .claim__small{font-size:36px;color:var(--blue-light)}
  .claim__big{font-size:54px}
  .seal{position:absolute;left:148px;top:332px;width:214px;height:214px}
  .home-icon{position:absolute;left:207px;top:582px;width:101px;height:86px}
  .brand{position:absolute;left:0;top:720px;width:100%;text-align:center;font-family:'Open Sans',sans-serif;font-weight:700;font-size:62px;color:var(--teal);letter-spacing:1px;line-height:1}

  /* back */
  .copy{position:absolute;left:28px;width:457px;font-family:'Open Sans',sans-serif;color:var(--ink);text-align:justify;letter-spacing:-0.3px}
  .copy--marketing{top:60px;font-size:15px;line-height:18px}
  .copy--legal{top:356px;font-size:13.6px;line-height:18.6px;color:var(--ink-soft)}
  .uses{position:absolute;left:0;top:198px;width:100%;height:140px}
  .use{position:absolute;width:110px;text-align:center}
  .use svg{display:block;margin:0 auto;width:104px;height:104px}
  .use__name{display:block;margin-top:6px;font-family:'Open Sans',sans-serif;font-size:14px;color:var(--teal);letter-spacing:0.3px}
  .volume{position:absolute;left:74px;top:590px;font-family:'Open Sans',sans-serif;font-size:26px;color:var(--ink)}
  .hazards{position:absolute;left:268px;top:566px;width:220px;height:116px}
  .maker{position:absolute;left:46px;top:700px;font-family:'Open Sans',sans-serif;font-size:15px;line-height:18px;color:var(--ink-soft)}
  .maker__web{display:block;margin-top:20px}
  .barcode-box{position:absolute;left:200px;top:694px;width:286px;height:110px;border:1.5px solid var(--frame);display:flex;align-items:center;justify-content:center;font-family:'Open Sans',sans-serif;font-size:16px;color:var(--ink)}
</style>
</head>
<body>
<main class="canvas">

  <section class="label label--front" aria-label="Etiqueta frontal">
    <div class="band band--top"></div>
    <h1 class="title">Limpiador<br>Higienizante</h1>
    <p class="claim"><span class="claim__small">CON</span> <span class="claim__big">ALCOHOL</span></p>

    <svg class="seal" viewBox="0 0 214 214" role="img" aria-label="Sello de calidad: sin perfume, sin colorantes">
      <circle cx="107" cy="107" r="105" fill="var(--red)"/>
    </svg>

    <svg class="home-icon" viewBox="0 0 101 86" role="img" aria-label="Uso doméstico">
      <rect x="3" y="3" width="95" height="80" rx="16" fill="#fff" stroke="var(--seal-dark)" stroke-width="4"/>
      <path d="M16 45 L50 18 L85 45 L77 45 L77 70 L24 70 L24 45 Z" fill="var(--blue)"/>
      <rect x="38" y="52" width="10" height="18" fill="#fff"/>
      <rect x="55" y="51" width="11" height="9" fill="#fff"/>
    </svg>

    <p class="brand">belvora</p>
    <div class="band band--bottom"></div>
  </section>

  <section class="label label--back" aria-label="Etiqueta trasera">
    <div class="band band--top"></div>

    <p class="copy copy--marketing">Limpiador higienizante para todo tipo de superfícies lavables. Su gran poder limpiador e higienizante elimina eficazmente la suciedad de zonas de contacto tales como asientos, inodoros, duchas, vidrios, pomos, manetas, asideros, barandillas, mesas, encimeras, suelos, mostradores, vitrinas, etc. No contiene lejía.</p>

    <div class="uses">
      <div class="use" style="left:12px">
        <svg viewBox="0 0 104 104" role="img" aria-label="Baños">
          <defs><linearGradient id="use-fill" x1="0" y1="0" x2="1" y2="1"><stop offset="0" stop-color="var(--teal-light)"/><stop offset="1" stop-color="var(--teal-dark)"/></linearGradient></defs>
          <circle cx="52" cy="52" r="50" fill="url(#use-fill)"/>
          <g fill="#fff">
            <rect x="34" y="22" width="18" height="26" rx="2"/>
            <path d="M30 50 H74 Q74 64 60 68 L62 82 H40 L42 66 Q30 62 30 50 Z"/>
          </g>
        </svg>
        <span class="use__name">BAÑOS</span>
      </div>
      <div class="use" style="left:128px">
        <svg viewBox="0 0 104 104" role="img" aria-label="Coches">
          <circle cx="52" cy="52" r="50" fill="url(#use-fill)"/>
          <g fill="#fff">
            <path d="M26 52 L32 36 Q34 32 40 32 H64 Q70 32 72 36 L78 52 Q82 54 82 58 V70 H22 V58 Q22 54 26 52 Z"/>
            <rect x="26" y="70" width="10" height="8" rx="2"/><rect x="68" y="70" width="10" height="8" rx="2"/>
          </g>
          <path d="M34 50 L38 38 H66 L70 50 Z" fill="var(--teal)"/>
          <circle cx="32" cy="60" r="3.5" fill="var(--teal)"/><circle cx="72" cy="60" r="3.5" fill="var(--teal)"/>
        </svg>
        <span class="use__name">COCHES</span>
      </div>
      <div class="use" style="left:266px">
        <svg viewBox="0 0 104 104" role="img" aria-label="Asientos">
          <circle cx="52" cy="52" r="50" fill="url(#use-fill)"/>
          <g fill="none" stroke="#fff" stroke-width="6" stroke-linecap="round" stroke-linejoin="round">
            <path d="M32 26 L40 62 H72"/>
            <path d="M46 50 H66"/>
            <path d="M36 78 H72"/>
            <path d="M54 62 V78"/>
          </g>
        </svg>
        <span class="use__name">ASIENTOS</span>
      </div>
      <div class="use" style="left:382px">
        <svg viewBox="0 0 104 104" role="img" aria-label="Puertas">
          <circle cx="52" cy="52" r="50" fill="url(#use-fill)"/>
          <rect x="34" y="22" width="20" height="60" rx="10" fill="none" stroke="#fff" stroke-width="5"/>
          <rect x="40" y="36" width="40" height="10" rx="5" fill="#fff"/>
          <rect x="41" y="58" width="6" height="12" rx="3" fill="#fff"/>
        </svg>
        <span class="use__name">PUERTAS</span>
      </div>
    </div>

    <p class="copy copy--legal">Líquido y vapores muy inflamables. Provoca irritación ocular grave. Puede provocar somnolencia o vértigo. Mantener alejado del calor, de superficies calientes, de chispas, de llamas abiertas y de cualquier otra fuente de ignición. No fumar. Mantener el recipiente herméticamente cerrado. Evitar respirar el polvo/el humo/el gas/la niebla /los vapores /el aerosol. Llevar guantes/prendas/gafas/máscara de protección. En caso de incendio emplear niebla de agua, espuma, productos químicos secos o dióxido de carbono ( CO2 ) para apagarlo. Almacenar en un lugar bien ventilado. Mantener el recipiente cerrado herméticamente. Mantener en lugar fresco.</p>

    <p class="volume">1L ℮</p>

    <svg class="hazards" viewBox="0 0 220 116" role="img" aria-label="Pictogramas de peligro: irritante e inflamable">
      <g transform="translate(55 58)">
        <rect x="-38" y="-38" width="76" height="76" transform="rotate(45)" fill="#fff" stroke="#d8262c" stroke-width="5"/>
        <rect x="-4.5" y="-27" width="9" height="34" rx="3" fill="#111"/>
        <circle cx="0" cy="18" r="5.5" fill="#111"/>
      </g>
      <g transform="translate(167 56)">
        <rect x="-36" y="-36" width="72" height="72" transform="rotate(45)" fill="#fff" stroke="#d8262c" stroke-width="5"/>
        <path d="M0 -28 C10 -17 17 -7 15 6 C13 15 8 19 0 19 C-9 19 -14 13 -14 4 C-14 -6 -8 -10 -6 -17 C-3 -11 -2 -8 0 -6 C2 -13 2 -21 0 -28 Z" fill="#111"/>
        <rect x="-15" y="24" width="30" height="4" fill="#111"/>
      </g>
    </svg>

    <p class="maker">Manufacture:<br>Adress<span class="maker__web">belvorahogar.com</span></p>

    <div class="barcode-box">BARCODE</div>

    <div class="band band--bottom"></div>
  </section>

</main>
</body>
</html>
```